Dental FAQ/advert tri-fold for holistic family dentist

We are a dental clinic with a holistic emphasis. We are seeking new clients, mainly middle classed families. A tri-fold brochure that is both a useful dental FAQ to keep in the house and acts as an advertisement for our clinic. It will be mailed out. It needs to look clean, modern, somewhat minimalist, and I want it to follow the Orble design esthetic. website is willowcrestdentalcare.com
Updates

I just updated the pamphlet file with revised text! Thanks for the nice designs so far, keep em coming.

Target Market(s)

Young families. Upper middle classes.

Industry/Entity Type

Dental

Requirements
Must have
• Follows our logo and colours.

```html
<!DOCTYPE html>
<html lang="en">
<head>
<meta charset="utf-8">
<title>Frequently Asked Questions For Your Dentist – Willowcrest Dental Care</title>
<link rel="stylesheet" href="https://fonts.googleapis.com/css2?family=Arimo:wght@400;700&display=swap">
<style>
  :root{
    --page:#eceae6;
    --paper:#ffffff;
    --blue:#2294dc;
    --green:#3aa545;
    --navy:#1c2b86;
    --body:#6d6f73;
    --faint:#e9eaec;
    --photo-a:#eef1f4;
    --photo-b:#cfd8e2;
  }
  *{margin:0;padding:0;box-sizing:border-box}
  html,body{width:992px;height:1200px;overflow:hidden}
  body{background:var(--page);font-family:"Arimo",Arial,sans-serif;position:relative}
  .sheet{position:absolute;left:118px;width:754px;height:528px;background:var(--paper);overflow:hidden}
  .sheet--outside{top:60px;display:grid;grid-template-columns:1fr 1fr 1fr}
  .sheet--inside{top:612px;display:flex;flex-direction:column}
  .panel{position:relative;padding:34px 22px 0 28px}
  .panel--blue{background:var(--blue);color:#fff}
  h3{font-size:9.6px;font-weight:400;color:var(--navy);line-height:12px;margin-bottom:6px}
  p{font-size:9px;line-height:11.5px;color:var(--body);text-align:justify;margin-bottom:14px}
  .panel--blue p,.band p{color:#fff}
  .panel--blue h3{color:var(--navy)}
  .photo{position:absolute;left:14px;bottom:0;width:144px;height:240px;
    background:radial-gradient(ellipse at 50% 65%,var(--photo-b),var(--photo-a) 70%,var(--paper))}
  .cover{display:flex;flex-direction:column;align-items:flex-end;padding:110px 24px 0 20px}
  .title{color:var(--green);font-weight:700;font-size:27px;line-height:29px;text-align:right;letter-spacing:-0.5px}
  .title .cap{font-size:38px}
  .brand{display:flex;align-items:center;gap:8px;margin-top:70px;align-self:center}
  .brand-dot{width:26px;height:26px;border-radius:50%;background:var(--blue)}
  .brand-name{color:var(--green);font-weight:400;font-size:17px;line-height:20px}
  .band{background:var(--green);flex:0 0 248px;display:grid;grid-template-columns:1fr 1fr 1fr}
  .band .col{padding:24px 16px 0 24px}
  .band h3{font-size:9.2px;line-height:11.5px;margin-bottom:5px}
  .band p{font-size:8.7px;line-height:10.9px;margin-bottom:11px}
  .band p:last-child{margin-bottom:0}
  .lower{position:relative;flex:1 1 auto;display:grid;grid-template-columns:1fr 1fr 1fr;overflow:hidden}
  .lower .col{position:relative;z-index:1;padding:16px 16px 0 24px}
  .lower h3{font-size:9.2px;line-height:11.5px;margin-bottom:5px}
  .lower p{font-size:8.7px;line-height:10.9px;margin-bottom:12px}
  .faq-mark{position:absolute;left:0;right:0;bottom:-60px;display:flex;justify-content:space-around;
    font-weight:700;font-size:380px;line-height:1;color:var(--faint);z-index:0}
</style>
</head>
<body>

<section class="sheet sheet--outside">
  <div class="panel">
    <h3>How can I manage my sensitive teeth?</h3>
    <p>Using a soft bristled toothbrush as well as desensitizing toothpaste is helpful, but many people still experience painful teeth sensitivity. We are pleased to offer effective laser desensitization, which is both gentle and painless. Other dental procedures that may help reduce sensitivity include using white fillings or applying dentin sealers to cover exposed root surfaces. Using a custom fit mouth guard to can also prevent further enamel wear.</p>
    <h3>Do I need to have my wisdom teeth removed?</h3>
    <p>While some people keep their wisdom teeth well into adulthood, wisdom teeth often do not grow in properly and need to be removed before a problem arises. This usually happens between the ages of 16-22. Our dentist will be able to assess your wisdom teeth and provide proper treatment.</p>
    <div class="photo" role="img" aria-label="Photo of a smiling dentist in a white coat"></div>
  </div>

  <div class="panel panel--blue">
    <h3>What can cause a toothache?</h3>
    <p>Toothaches are caused by an irritated nerve within the tooth, by or an infection surrounding the tooth. Prior to your dental appointment an over the counter pain medication such as ibuprofen will usually provide temporary relief. At your visit, our dentist will determine the exact cause of the problem and provide treatment options.</p>
    <h3>What should I do if I knock a tooth out?</h3>
    <p>Say sorry to the other person! Just kidding, if a tooth is knocked clear out, it can sometimes be re-implanted, if done within 30-60 minutes. Gently rinse the tooth off, and store it in a solution of milk or clean water and make your way to a dentist as soon as possible.</p>
    <h3>Should I wear a mouth guard during recreational activities?</h3>
    <p>Mouth guards should be used by anyone who plays contact sports such as hockey, football, boxing, soccer, basketball, and lacrosse. Your dentist can create a custom appliance that provides much more comfort and protection than a store-bought appliance.</p>
    <h3>What's the difference between teeth whitening in a dental office and store bought kits?</h3>
    <p>Our dental clinic can supply you with a custom fit tray to maximize your teeth whitening. Our dental office is able to prescribe stronger formulations of the whitening solution for a longer lasting, whiter smile.</p>
  </div>

  <div class="cover">
    <h1 class="title">
      <span class="cap">F</span>requently<br>
      <span class="cap">A</span>sked<br>
      <span class="cap">Q</span>uestions<br>
      For Your<br>
      <span class="cap">D</span>entist
    </h1>
    <div class="brand">
      <span class="brand-dot"></span>
      <span class="brand-name">Willowcrest<br>Dental Care</span>
    </div>
  </div>
</section>

<section class="sheet sheet--inside">
  <div class="band">
    <div class="col">
      <h3>When should my child first start visiting the dentist?</h3>
      <p>The Northfield Dental Council recommends bringing your children to visit the dentist 6 months after their first tooth has appeared. We recommend bringing children in for short "happy visits" that build their confidence and comfort in being at our dental clinic. A happy visit is free unless dental services are provided. Children can observe your appointments and they can learn the fun parts of the dental visit such as counting and polishing teeth, and riding up and down in the dental chair. And of course, the best part, the prize drawer at the end of the appointment! We find that children who come for happy visits experience little to no dental fear or anxiety in their coming years.</p>
    </div>
    <div class="col">
      <h3>Can I visit the dentist if I am pregnant?</h3>
      <p>Regular dental cleanings are especially important during pregnancy, as pregnancy gingivitis affects up to 50-70% of pregnant women. Gum disease has been linked to low birth weight and premature delivery. We recommend a thorough dental exam and cleaning if you are pregnant or planning on having a baby.</p>
      <h3>What are some of the latest technologies available for improving my oral health?</h3>
      <p>Dentistry is always evolving and your treatment and safety can be reinforced with new technologies. For example, digital x-rays can greatly reduce your exposure to radiation. Lasers are a non-invasive way to quickly and easily kill bacteria below your gum line. Speed braces can straighten your teeth much faster than traditional braces.</p>
    </div>
    <div class="col">
      <h3>Are amalgam fillings containing mercury safe?</h3>
      <p>The Public Health Board's official position states that amalgams are safe, but should be avoided in certain people with medical conditions. It is best to consult with your dentist directly. Mercury-free options for dental care are available, and we offer a specific and safe method of mercury removal.</p>
      <h3>What are dental sealants, and do they contain BPA?</h3>
      <p>Dental sealants are a way to protect a tooth from forming a cavity by sealing the natural pits and grooves in a tooth with resin. Some sealants do not contain Bis-phenol A, and you may ask your dentist if the type of material used has BPA.</p>
    </div>
  </div>

  <div class="lower">
    <div class="faq-mark" aria-hidden="true"><span>F</span><span>A</span><span>Q</span></div>
    <div class="col">
      <h3>How often should I get dental checkups and cleanings?</h3>
      <p>Everybody is different, and has different needs when it comes to regular examinations and cleanings. Most people need to have their teeth cleaned at least every 6 months. Those with gum disease present may require more frequent appointments.</p>
      <h3>How do I know my dental office is clean?</h3>
      <p>Dental offices in Alberta follow the most stringent regulations in the world for sterilization and infection control. The operatory's are cleaned between every patient, staff members thoroughly wash their hands regularly, and items are put through an auto-clave system for sterilization. Our dental staff members would be happy to show you exactly how your safety is protected.</p>
    </div>
    <div class="col">
      <h3>How can I get my records transferred to a new dental office?</h3>
      <p>It's as simple as asking your former dental office to send the records to the new office. Sometimes you may be requested to sign a release and consent form as well. We are happy to help you with the process.</p>
      <h3>Is fluoride safe?</h3>
      <p>The Family Health Measures Survey 2007-2009 found that 16% of children have mild forms of dental fluorosis that often go unnoticed. Dental fluorosis is a change in the appearance of teeth, often causing small white specks to appear. It is caused when higher than optimal amounts of fluoride are ingested in early childhood. Fluoride-free options for dental care are available at our office.</p>
    </div>
    <div class="col">
      <h3>What is gum disease and how can it affect my health?</h3>
      <p>Gum disease, or periodontal disease, is when bacteria and tartar on your teeth cause inflammation of the gums and the bone supporting your teeth. When severe enough, bone loss occurs, leading to loose teeth and gum abscesses. Gum disease can be treated by daily flossing and regular dental cleaning appointments. Our dentist and dental hygienists will be able to discuss treatment options available for you.</p>
      <h3>What do I do about bad breath?</h3>
      <p>80% of bad breath comes from an oral source. For instance, cavities, cracked fillings, gum disease, and less-than-clean dentures can all lead to bad breath. An examination by our dentist will discover the source of the problem, and frequent and thorough dental cleanings will often alleviate this embarrassing problem.</p>
    </div>
  </div>
</section>

</body>
</html>
```